Business Card Design Project

Hello Designers, hope you are all aiming enjoy the weekend
I have the Business Logo (uploaded), you can alter the color which ever way you think would work,
Im looking for a simple yet striking feel, something which will stay memorable (I have uploaded 3 examples for you to flick through)
Information on the card, will just be the bare minimum,
Double Sided
Info being
i.e.
Name
Number
Website
ABN
Teo Marlowick
+482710365 (singapore)
+615093284 (Australia)
+790428153 (America)
www.lumoren-match.example
ABN 90817263
Enjoy,
Teo

```html
<!DOCTYPE html>
<html lang="en">
<head>
<meta charset="utf-8">
<title>Lumoren Match — Business Cards</title>
<link href="https://fonts.googleapis.com/css2?family=Questrial&display=swap" rel="stylesheet">
<style>
  :root {
    --page: #ffffff;
    --card-light: #ffffff;
    --card-dark: #231f20;
    --ink-grey: #58595b;
    --ink-light: #ffffff;
    --green: #6abf3f;
    --magenta: #cc3a96;
    --yellow: #e6e31b;
  }
  html, body {
    margin: 0;
    width: 1200px;
    height: 1200px;
    overflow: hidden;
    background: var(--page);
    font-family: "Questrial", "Helvetica Neue", Arial, sans-serif;
  }
  .card {
    position: absolute;
    width: 538px;
    height: 220px;
    box-shadow: 0 4px 10px rgba(0,0,0,0.22);
    box-sizing: border-box;
  }
  .card--light { background: var(--card-light); color: var(--ink-grey); }
  .card--dark { background: var(--card-dark); color: var(--ink-light); }
  .set--green { --accent: var(--green); }
  .set--magenta { --accent: var(--magenta); }
  .set--yellow { --accent: var(--yellow); }

  .card__front { display: flex; align-items: center; justify-content: center; }
  .brand { display: flex; align-items: center; gap: 12px; }
  .brand__mark {
    width: 26px; height: 26px;
    background: var(--accent);
    border-radius: 5px;
  }
  .brand__name {
    font-size: 34px;
    letter-spacing: 0.5px;
    color: inherit;
  }
  .card--light .brand__name { color: var(--ink-grey); }

  .dots {
    position: absolute;
    left: 64px;
    top: 54px;
    width: 405px;
    height: 27px;
    background: radial-gradient(circle, var(--accent) 5.5px, transparent 6.3px) 0 0 / 27px 27px repeat-x;
  }
  .contact {
    position: absolute;
    right: 78px;
    top: 92px;
    text-align: right;
    text-transform: uppercase;
  }
  .contact__name {
    font-size: 17px;
    letter-spacing: 2.6px;
    color: var(--accent);
    margin: 0 0 10px;
  }
  .contact__line {
    font-size: 12px;
    letter-spacing: 1.2px;
    line-height: 21px;
    margin: 0;
  }
</style>
</head>
<body>

<section class="set set--green">
  <div class="card card--light card__front" style="left:60px; top:132px;">
    <div class="brand"><span class="brand__mark"></span><span class="brand__name">Lumoren Match</span></div>
  </div>
  <div class="card card--light card__back" style="left:609px; top:132px;">
    <div class="dots"></div>
    <div class="contact">
      <p class="contact__name">Teo Marlowick</p>
      <p class="contact__line">+482710365 (Singapore) +615093284 (Australia)</p>
      <p class="contact__line">+790428153 (America) www.lumoren-match.example</p>
      <p class="contact__line">ABN 90817263</p>
    </div>
  </div>
</section>

<section class="set set--magenta">
  <div class="card card--light card__front" style="left:60px; top:402px;">
    <div class="brand"><span class="brand__mark"></span><span class="brand__name">Lumoren Match</span></div>
  </div>
  <div class="card card--light card__back" style="left:609px; top:402px;">
    <div class="dots"></div>
    <div class="contact">
      <p class="contact__name">Teo Marlowick</p>
      <p class="contact__line">+482710365 (Singapore) +615093284 (Australia)</p>
      <p class="contact__line">+790428153 (America) www.lumoren-match.example</p>
      <p class="contact__line">ABN 90817263</p>
    </div>
  </div>
</section>

<section class="set set--yellow">
  <div class="card card--dark card__front" style="left:60px; top:790px;">
    <div class="brand"><span class="brand__mark"></span><span class="brand__name">Lumoren Match</span></div>
  </div>
  <div class="card card--dark card__back" style="left:609px; top:790px;">
    <div class="dots"></div>
    <div class="contact">
      <p class="contact__name">Teo Marlowick</p>
      <p class="contact__line">+482710365 (Singapore) +615093284 (Australia)</p>
      <p class="contact__line">+790428153 (America) www.lumoren-match.example</p>
      <p class="contact__line">ABN 90817263</p>
    </div>
  </div>
</section>

</body>
</html>
```